Brellow Business Card Re-design

Our current cards are outdated. This is our website www.brellowinsight.com. We would like something that is "on-brand" and consistent with our social media sites. We are strategic consultants with a core competency in Marketing Research. Although, please know we are considering a brand logo redesign and potentially a new look. If we like your work here we will invite you to participate when we get to that project. Thank you very much. Corabel
Here are our social sites: https://chirvalo.com/Brellow?lang=en
https://plus.quarnix.com/+Brellowinsight
https://www.workvelt.com/company/4958207/
https://www.friendlumo.com/BrellowInc/
Project Deadline Extended Reason: We appreciate the designs that have been submitted. We are extending the deadline because not everyone in our office has been available until now to view the designs. Thank you. Added Monday, September 25, 2017
Industry/Entity Type
Business
Look and feel

```html
<!DOCTYPE html>
<html lang="en">
<head>
<meta charset="utf-8">
<title>Brellow Business Card</title>
<link rel="stylesheet" href="https://fonts.googleapis.com/css2?family=Poppins:wght@400;500;600&display=swap">
<style>
  :root {
    --brand-green: #6abf4b;
    --ink: #2b2b2b;
    --paper: #ffffff;
    --backdrop: #2a2a2a;
    --dot: #e7f4e0;
  }
  html, body {
    margin: 0;
    width: 1200px;
    height: 852px;
    overflow: hidden;
    background: var(--backdrop);
    font-family: "Poppins", sans-serif;
  }
  .card {
    position: absolute;
    left: 300px;
    width: 600px;
    height: 343px;
    box-sizing: border-box;
    overflow: hidden;
  }
  .card-front {
    top: 56px;
    background: var(--brand-green);
  }
  .card-back {
    top: 439px;
    background: var(--paper);
    border-bottom: 12px solid var(--brand-green);
  }
  .wordmark {
    font-weight: 600;
    letter-spacing: 1px;
    line-height: 1;
  }
  .card-front .wordmark {
    position: absolute;
    top: 110px;
    left: 0;
    right: 0;
    text-align: center;
    color: var(--paper);
    font-size: 64px;
  }
  .social-row {
    position: absolute;
    top: 262px;
    left: 0;
    right: 0;
    display: flex;
    justify-content: center;
    gap: 14px;
  }
  .social-dot {
    width: 16px;
    height: 16px;
    border-radius: 50%;
    background: var(--dot);
  }
  .card-back .wordmark {
    position: absolute;
    top: 30px;
    right: 36px;
    color: var(--brand-green);
    font-size: 34px;
  }
  .holder {
    position: absolute;
    top: 120px;
    left: 40px;
  }
  .holder-name {
    margin: 0;
    color: var(--brand-green);
    font-weight: 600;
    font-size: 19px;
    text-transform: uppercase;
    letter-spacing: 0.3px;
  }
  .holder-role {
    margin: 2px 0 0 14px;
    color: var(--ink);
    font-size: 12px;
  }
  .address {
    position: absolute;
    top: 125px;
    right: 36px;
    text-align: right;
    color: var(--ink);
    font-size: 12.5px;
    line-height: 1.5;
    font-style: normal;
  }
  .contacts {
    position: absolute;
    left: 40px;
    bottom: 26px;
    margin: 0;
    padding: 0;
    list-style: none;
    color: var(--ink);
    font-size: 13px;
    line-height: 1.55;
  }
  .contacts li {
    display: flex;
    align-items: center;
    gap: 10px;
  }
  .contacts svg {
    width: 10px;
    height: 10px;
    fill: var(--brand-green);
  }
  .accent { color: var(--brand-green); }
</style>
</head>
<body>
  <section class="card card-front" aria-label="Card front">
    <div class="wordmark">brellow</div>
    <div class="social-row" aria-label="Social channels">
      <span class="social-dot"></span><span class="social-dot"></span>
      <span class="social-dot"></span><span class="social-dot"></span>
      <span class="social-dot"></span><span class="social-dot"></span>
      <span class="social-dot"></span><span class="social-dot"></span>
    </div>
  </section>

  <section class="card card-back" aria-label="Card back">
    <div class="wordmark">brellow</div>
    <div class="holder">
      <h1 class="holder-name">Halvard Presk</h1>
      <p class="holder-role">Director</p>
    </div>
    <address class="address">14 Tollery Lane<br>Dunmore, England, Q4 2XB</address>
    <ul class="contacts">
      <li>
        <svg viewBox="0 0 10 10" aria-hidden="true"><path d="M2 0.5 L3.6 0.5 L4.2 3 L3 3.8 Q4 6 6.2 7 L7 5.8 L9.5 6.4 L9.5 8 Q9.5 9.5 8 9.5 Q0.5 9 0.5 2 Q0.5 0.5 2 0.5Z"/></svg>
        555.201.3948
      </li>
      <li>
        <svg viewBox="0 0 10 10" aria-hidden="true"><path d="M0.5 2 H9.5 V8.5 H0.5Z M1.3 2.6 L5 5.4 L8.7 2.6" fill="none" stroke="#6abf4b" stroke-width="1.1"/></svg>
        info@brellowinsight.com
      </li>
      <li>
        <svg viewBox="0 0 10 10" aria-hidden="true"><g fill="none" stroke="#6abf4b" stroke-width="1"><circle cx="5" cy="5" r="4.3"/><ellipse cx="5" cy="5" rx="1.9" ry="4.3"/><path d="M0.7 5 H9.3"/></g></svg>
        <span>www.<span class="accent">brellowinsight</span>.com</span>
      </li>
    </ul>
  </section>
</body>
</html>
```